Northvale Beam Works

We manufacture and distribute luminaires for industrial lighting applications. We cover the European market. We look for a basic well designed web site, with not too much text, as we're gonna do it multilingual. Requirements: a.) Wordpress Avada Theme b.) Pages: 1. Start (compare http://www.brimtek.co.kr/rb/?r=en and www.vorlanz.de for slides => mixed products & industry photos) 2. Company (short description) http://www.vorlanz.de/en/company/about-us, european map with offices in Stockholm (Sweden), Berlin Heidelberg (Germany), Linz (Austria) Description fill in : "The name of NBW stands for competence and quality in all areas of technical light fittings: waterproof / dustproof light fittings - industrial-grade light fittings - outdoor luminaires - A very high level of reliability, of competence and innovation their mark on thinking and actions of people working in the family company. NBW for a very long time: research and development, laboratory work, toolmaking, polyester pressing plant, sheet metal forming, powder coating and assembly are concentrated in NBW's own premises. Worldwide innovations have helped NBW over and over again to launch new impulses to the market. For decades now NBW has been one of the leading bidders of this industrial sector. The international significance of NBW as a lighting specialist is based on intelligent and useful solutions - not just with respect to standard products but as far as branch-specific technical problems or application conditions and particular customer wishes are concerned. "3. Products [pls. see infographic under https://www.kampera.com/en/applications/industry/lighting-for-industry/ [we are looking for something similar to start on top, then short description product with download pdf] 4. News (Events, new products, etc.) 5. Partner login (for downloads of further data, well structured) 6. Contact (4 office adresses, map, no contact form) c.) Logo / Colors: 1 Logo with 2 different colors, please choose either blue or red one or the colors according to your recommendation d.) What do we do? High quality industrial lighting smart lighting control e.) Industries: Look at this photo here for a glimpse: http://www.dorv-technik.de/lichttechnik f.) Areas: Look at the infographic here, to get an idea which areas of lighting / products we are covering: https://www.kampera.com/en/applications/industry/lighting-for-industry/ => Design / Associations: Fresh, clear, technology, high quality, solidity, reliability experience like https://www.kampera.com/en/applications/industry/lighting-for-industry/ Thank you very much for your offers!

Target Market(s)

Resellers / Wholesalers of industrial luminaires AND direct clients (industrial, commercial)

Industry/Entity Type

Light Industrial

Coding

Coded - Design and coding required

Number of Pages Required

5+ page

Font styles to use
Sans Serif

Colors
0355a3
ec1f27

Requirements
Must have
• a.) Wordpress Avada Theme b.) Pages: 1. Start / 2. Company (short description, european map with offices in Stockholm (Sweden), Berlin Heidelberg (Germany), Linz (Austria) / 3. Products [pls infographic under f.) => News (Events, new products, etc.) / 5. Partner Login (for Downloads) / 6. Contact c.) Logo / Colors: 1 Logo with 2 different colors, please choose either blue or red one or the colors according to your recommendation d.) What do we do? High quality industrial lighting smart lighting control e.) Industries: Look at this photo here for a glimpse: http://www.dorv-technik.de/lichttechnik f.) Areas: Look at the infographic here, to get an idea which areas of lighting / products we are covering: https: //www.kampera. com / en / applications / industry / lighting-for-industry / => Design / Associations: Fresh, clear, technology, high quality, solidity, reliability experience => tidy look
Nice to have
• - some nice WP Avada elements - map with locations (see b.) 2.) above) - infographic (see f.) above)
Should not have
• not too overloaded, not too crowded

```html
<!DOCTYPE html>
<html lang="en">
<head>
<meta charset="utf-8">
<title>Northvale Beam Works — Industrial Lighting</title>
<link rel="stylesheet" href="https://fonts.googleapis.com/css2?family=Lato:ital,wght@0,300;0,400;0,700;1,400&family=Open+Sans:wght@400;600&display=swap">
<style>
  :root{
    --blue:#0355a3;
    --blue-deep:#0b3f8f;
    --navy:#0d2f6e;
    --red:#ec1f27;
    --ink:#222;
    --grey-text:#777;
    --nav-bg:#e9e9e9;
    --section-grey:#e1e1e1;
    --white:#fff;
    --black:#000;
  }
  *{box-sizing:border-box;margin:0;padding:0}
  html,body{width:1200px;height:2782px;overflow:hidden}
  body{
    font-family:"Lato",sans-serif;color:var(--ink);position:relative;
    background:linear-gradient(180deg,#8d9298 0%,#a7abb0 20%,#9a9ea3 40%,#5c5f63 60%,#2a2b2d 75%,#1b1b1c 100%);
  }
  .backdrop{position:absolute;inset:0}
  .page{position:absolute;left:160px;top:0;width:880px;height:2782px}
  section,header,nav,footer{position:relative;width:880px;overflow:hidden}

  .site-header{height:108px;background:var(--white)}
  .brand{position:absolute;left:44px;top:34px;display:flex;align-items:center;gap:12px}
  .brand-mark{width:30px;height:30px;background:var(--red)}
  .brand-name{font-size:38px;font-weight:700;color:var(--red);letter-spacing:2px}
  .tagline{position:absolute;right:174px;top:40px;text-align:right;font-size:14px;line-height:20px;color:#666}
  .btn-info{position:absolute;left:723px;top:44px;width:113px;height:32px;background:var(--red);color:var(--white);font-size:11px;font-weight:700;display:flex;align-items:center;justify-content:center;letter-spacing:.5px}

  .main-nav{height:48px;background:var(--nav-bg)}
  .main-nav a{position:absolute;top:15px;transform:translateX(-50%);font-size:14px;font-weight:700;color:#222;text-decoration:none}
  .main-nav a.current{color:var(--red);font-weight:400}

  .hero{height:404px;background:radial-gradient(ellipse at 30% 60%,#8fb8ef 0%,#2f6fcf 35%,#0d3f9c 70%,#062a6e 100%)}
  .hero h1{position:absolute;top:138px;width:100%;text-align:center;color:var(--white);font-size:28px;font-weight:700;letter-spacing:.3px}
  .btn-dark{position:absolute;left:341px;top:182px;width:185px;height:37px;background:var(--navy);color:var(--white);font-size:13px;font-weight:700;display:flex;align-items:center;justify-content:center;letter-spacing:.5px}

  .about{height:362px;background:var(--white);text-align:center}
  .about h2{padding-top:52px;font-size:30px;font-weight:300;color:#111}
  .about p{font-family:"Open Sans",sans-serif;font-size:12.5px;line-height:20px;color:var(--grey-text);width:700px;margin:0 auto}
  .about p.first{margin-top:26px}
  .about p+p{margin-top:12px}
  .link-red{display:inline-block;margin-top:20px;font-size:14px;font-weight:700;color:var(--red)}

  .testimonial{height:321px;background:linear-gradient(180deg,#3c3c3c 0%,#242424 55%,#3a3a3a 100%);text-align:center;color:var(--white)}
  .testimonial blockquote{padding-top:106px;font-size:16.5px;font-style:italic;line-height:29px}
  .testimonial cite{display:block;margin-top:12px;font-style:normal;font-weight:700;font-size:14px}
  .dots{position:absolute;top:232px;left:0;width:100%;display:flex;justify-content:center;gap:8px}
  .dots span{width:11px;height:11px;border-radius:50%;background:var(--white)}
  .dots span.hollow{background:transparent;border:2px solid var(--white)}

  .banner{height:98px;background:var(--red);display:flex;align-items:center;justify-content:center;gap:14px;color:var(--white);font-size:21px;font-weight:700}

  .products{height:486px;background:var(--section-grey)}
  .products h2{text-align:center;padding-top:50px;font-size:28px;font-weight:400;color:#111}
  .product-grid{position:absolute;left:44px;top:115px;display:flex;gap:22px}
  .product-card{width:168px;height:204px;background:var(--white)}
  .product-photo{height:111px;background:linear-gradient(180deg,#f4f4f4,#cfd2d6)}
  .product-card h3{font-size:14px;font-weight:400;color:var(--blue);padding:12px 17px 4px}
  .product-card p{font-family:"Open Sans",sans-serif;font-size:9.5px;line-height:15px;color:#555;padding:0 17px}
  .cta-bar{position:absolute;left:46px;top:366px;width:734px;height:69px;background:var(--blue-deep);color:var(--white);display:flex;align-items:center}
  .cta-title{margin-left:38px;font-size:14px;font-weight:700;width:238px}
  .cta-text{font-family:"Open Sans",sans-serif;font-size:9.5px;line-height:15px;color:#b9c9e6;width:290px}
  .cta-link{margin-left:42px;font-size:9.5px;font-weight:700}

  .split{height:533px;display:flex}
  .industries{width:426px;height:533px;background:linear-gradient(160deg,#7a2a18 0%,#1e3f7c 40%,#0f2856 100%);color:var(--white);padding:117px 44px 0 52px}
  .industries h2{font-size:25px;font-weight:400}
  .industries p{font-family:"Open Sans",sans-serif;font-size:12.5px;line-height:27.5px;margin-top:18px}
  .industries .more{display:block;margin-top:14px;font-size:12px;font-weight:700}
  .news{position:relative;width:454px;height:533px;background:var(--white);padding:40px 39px 0 39px}
  .news h2{font-size:23px;font-weight:400;color:var(--red)}
  .news-list{margin-top:30px}
  .news-item{display:flex;gap:17px;height:97px;margin-bottom:29px}
  .news-photo{width:111px;height:97px;flex:none;background:linear-gradient(180deg,#2f3e57,#8c949e)}
  .news-item h3{font-family:"Open Sans",sans-serif;font-size:12px;font-weight:400;line-height:17px;color:#333;margin-top:3px}
  .news-item time{display:block;margin-top:12px;font-family:"Open Sans",sans-serif;font-size:11px;color:#555}
  .view-all{position:absolute;left:39px;top:473px;width:376px;border-top:1px solid #777;border-bottom:1px solid #777;font-size:11px;font-weight:400;padding:5px 4px 5px;color:#222}

  .closing{height:297px;background:var(--blue-deep);text-align:center;color:var(--white)}
  .closing p{padding-top:80px;font-size:20.5px;line-height:30px}
  .btn-outline{display:inline-block;margin-top:22px;width:174px;height:37px;border:2px solid var(--white);font-size:12px;font-weight:700;line-height:33px}

  .site-footer{height:125px;background:var(--black);text-align:center;color:#888;font-family:"Open Sans",sans-serif;font-size:11px}
  .site-footer small{display:block;padding-top:33px;font-size:11px}
  .social{display:flex;justify-content:center;gap:4px;margin-top:18px}
</style>
</head>
<body>
<div class="backdrop" role="img" aria-label="Photo of an industrial hall with high-bay lighting, steel trusses and machinery"></div>
<div class="page">
  <header class="site-header">
    <div class="brand"><span class="brand-mark"></span><span class="brand-name">NBW</span></div>
    <p class="tagline">„The name of NBW stands for competence and<br>quality in all areas of technical light</p>
    <a class="btn-info">MORE INFO</a>
  </header>

  <nav class="main-nav">
    <a class="current" style="left:116px">HOME</a>
    <a style="left:241px">COMPANY</a>
    <a style="left:382px">PRODUCTS</a>
    <a style="left:508px">NEWS</a>
    <a style="left:628px">PARTNER</a>
    <a style="left:760px">CONTACT</a>
  </nav>

  <section class="hero" role="img" aria-label="Photo of LED bulbs and lamps lit in blue tones">
    <h1>WE ARE AN INDUSTRIAL LIGHTING COMPANY</h1>
    <a class="btn-dark">VIEW PRODUCTS</a>
  </section>

  <section class="about">
    <h2>About Our Company</h2>
    <p class="first">Halvorn light fittings are in the field on all continents and in almost every country of the world and Halvorn is one of the leading bidders of explosion-proof light fittings worldwide.</p>
    <p>Especially at large chemical and petrochemical plants, at offshore projects (drilling platforms) and at power stations the people rely on the high safety standard and on the excellent quality of the Halvorn luminaires. The family company is also facing up to its responsibility for the location in Germany: Since its formation in 1895 the Halvorn company with currently about 400 people is one of the most important employers in the region of Worms.</p>
    <a class="link-red">LEARN MORE</a>
  </section>

  <section class="testimonial" role="img" aria-label="Photo of a dark factory ceiling with hanging lights">
    <blockquote>aliquam Curabitur iaculis tempus eros Curabitur vel mi sit amet magna malesuada<br>ultrices Ut nisi erat fermentum vel congue id euismod in elit Fusce</blockquote>
    <cite>BY AUTHOR NAME</cite>
    <div class="dots"><span class="hollow"></span><span></span><span></span></div>
  </section>

  <section class="banner">
    <svg width="36" height="36" viewBox="0 0 36 36" fill="none" stroke="#fff" stroke-width="2" aria-hidden="true">
      <path d="M8 28 L20 16 L24 20 L12 32 Z"/><path d="M20 16 L26 10 L30 14 L24 20"/>
      <path d="M28 4 L29 8 M33 7 L30 9 M34 13 L31 12"/>
    </svg>
    <span>MORBI DIAM MAURIS VIVERRA IN GRAVIDA EU</span>
  </section>

  <section class="products">
    <h2>Our Products</h2>
    <div class="product-grid">
      <article class="product-card"><div class="product-photo" role="img" aria-label="Photo of an LED high-bay luminaire"></div><h3>Product Name</h3><p>Morbi diam mauris viverra in gravida eu mattis in ante</p></article>
      <article class="product-card"><div class="product-photo" role="img" aria-label="Photo of an outdoor post-top luminaire"></div><h3>Product Name</h3><p>Morbi diam mauris viverra in gravida eu mattis in ante</p></article>
      <article class="product-card"><div class="product-photo" role="img" aria-label="Photo of a pendant LED high-bay light"></div><h3>Product Name</h3><p>Morbi diam mauris viverra in gravida eu mattis in ante</p></article>
      <article class="product-card"><div class="product-photo" role="img" aria-label="Photo of an LED floodlight"></div><h3>Product Name</h3><p>Morbi diam mauris viverra in gravida eu mattis in ante</p></article>
    </div>
    <div class="cta-bar">
      <span class="cta-title">CHECK OUR MORE PRODUCTS</span>
      <span class="cta-text">Morbi diam mauris viverra in gravida eu mattis in ante Morbi eget arcu Morbi porta libero id ullamcorper nonummy</span>
      <span class="cta-link">CLICK HERE TO VIEW ALL</span>
    </div>
  </section>

  <section class="split">
    <div class="industries" role="img" aria-label="Photo of an industrial crane structure at dusk with floodlights">
      <h2>Industries we Serve</h2>
      <p>Halvorn light fittings are in the field on all continents and in almost every country of the world and Halvorn is one of the leading bidders of explosion-proof light fittings worldwide. Especially at large chemical and petrochemical plants, at offshore projects (drilling platforms) and at power stations the people rely on the high safety standard and on the excellent quality of the Halvorn luminaires.</p>
      <span class="more">LEARN MORE</span>
    </div>
    <div class="news">
      <h2>Neuheiten und Informationen</h2>
      <div class="news-list">
        <article class="news-item"><div class="news-photo" role="img" aria-label="Photo of an industrial site at night"></div><div><h3>Neu: LED-Notleuchten ClaroLed N - Modernste LED-Notleuchten für explosionsgefährdete Bereiche</h3><time>07.11.2017</time></div></article>
        <article class="news-item"><div class="news-photo" role="img" aria-label="Photo of a street lit by outdoor luminaires"></div><div><h3>NEU: VENTA Vario - Die universelle LED-Außenleuchte mit variabel einstellbarem Lichtstrom</h3><time>07.11.2017</time></div></article>
        <article class="news-item"><div class="news-photo" role="img" aria-label="Photo of a worker on a plant platform"></div><div><h3>LED-Feuchtraumleuchten von Halvorn - Qualität garantiert Das Wichtigste vorweg:</h3><time>07.11.2017</time></div></article>
      </div>
      <div class="view-all">VIEW ALL NEWS</div>
    </div>
  </section>

  <section class="closing">
    <p>Donec dictum lectus non odio Cras a ante vitae enim iaculis<br>aliquam Mauris nunc quam venenatis nec</p>
    <a class="btn-outline">LEARN MORE</a>
  </section>

  <footer class="site-footer">
    <small>© 2017 Company Name &nbsp;All right reserved &nbsp;Terms of Use</small>
    <div class="social">
      <svg width="120" height="28" viewBox="0 0 120 28" aria-hidden="true" fill="none" stroke="#777" stroke-width="1.5">
        <circle cx="15" cy="14" r="12"/><circle cx="45" cy="14" r="12"/><circle cx="75" cy="14" r="12"/><circle cx="105" cy="14" r="12"/>
      </svg>
    </div>
  </footer>
</div>
</body>
</html>
```